House Cleaning company in need of handout re-designs

We are looking to create a 2 sided, full color, 6" x 4" handout that promotes the company www.dustly.com

We have one in existence that performed well, but find it too busy and would like another one designed to test performance (please see the attached files for original design). We are looking for one additional design, however depending on quality of work submitted we will select up to 5 designs.

We are looking for clean designs the will improve performance and you are 'carte blanche' on the design. That said, please ensure the following elements are present:

1) Space for an offer (i.e $39 for 3 hours of cleaning) with an expiry date.
2) Unique URL
3) Promo Code
4) Phone Number
5) The tagline of "Let Dustly handle it" is present.
6) Logo
7) Brand colors are maintained

Also, please highlight the following:

*Eco-Friendly Cleaning Services
*Fully-Screened Cleaning Experts
*60-point checklist
*Easy Online Booking Process

Thank you.

House Cleaning

```html
<!DOCTYPE html>
<html lang="en">
<head>
<meta charset="utf-8">
<title>Dustly Handout</title>
<link href="https://fonts.googleapis.com/css2?family=Oswald:wght@300;400;500;600&family=Roboto:wght@400;700&display=swap" rel="stylesheet">
<style>
  :root{
    --teal:#2bbbad;
    --coral:#ef6b61;
    --yellow:#faf59c;
    --ink:#3b3b3b;
    --frame:#dcdcdc;
    --page:#2a2a2a;
    --white:#ffffff;
    --tick:#fde24f;
  }
  *{margin:0;padding:0;box-sizing:border-box}
  html,body{width:1200px;height:1000px;overflow:hidden;background:var(--page)}
  .canvas{position:relative;width:1200px;height:1000px}
  .card{position:absolute;left:273px;width:656px;height:436px;background:var(--white);border:8px solid var(--frame);overflow:hidden;font-family:"Roboto",Arial,sans-serif;color:var(--ink)}
  .card--front{top:55px}
  .card--back{top:509px}
  .abs{position:absolute}
  .text{z-index:2}
  .cond{font-family:"Oswald","Arial Narrow",sans-serif}

  /* front */
  .kicker{left:20px;top:14px;font-size:25px;font-weight:400;letter-spacing:-.2px;white-space:nowrap;line-height:1.3}
  .headline{left:19px;top:34px;font-size:62px;font-weight:400;line-height:1.3;color:var(--teal);letter-spacing:-.5px;white-space:nowrap}
  .band{left:0;top:123px;width:430px;height:133px;background:var(--yellow);z-index:0}
  .photo{top:130px;height:118px;border:3px solid #cfcfcf;z-index:1}
  .photo--family{left:19px;width:140px;background:linear-gradient(135deg,#f3ece6,#d8b59c 60%,#eee)}
  .photo--kitchen{left:163px;width:138px;background:linear-gradient(160deg,#e9ecef,#b9c3ca 55%,#c89a6b)}
  .hero{left:305px;top:0;width:335px;height:420px;z-index:1;background:radial-gradient(ellipse 60% 55% at 58% 45%,rgba(242,212,194,.9) 0,rgba(232,246,245,.8) 45%,rgba(246,251,253,0) 80%)}
  .book{left:20px;top:264px;font-size:27px;font-weight:300;white-space:nowrap;line-height:1.3}
  .brand{color:var(--coral);font-weight:700;font-family:"Roboto",Arial,sans-serif}
  .brand small{font-size:.45em}
  .url{left:20px;top:304px;font-size:27px;font-weight:700;color:var(--teal);white-space:nowrap}
  .call{left:20px;top:338px;font-size:30px;font-weight:700;color:var(--teal);white-space:nowrap}
  .call b{color:var(--ink)}
  .promo{left:20px;top:378px;font-size:19px;white-space:nowrap}
  .promo sup{font-size:.55em}

  /* back */
  .tagline{left:20px;top:22px;font-size:33px;font-weight:500;color:var(--teal);white-space:nowrap;line-height:1.3}
  .logo{left:425px;top:22px;font-size:44px;white-space:nowrap}
  .intro{left:22px;top:84px;width:258px;font-size:16.5px;line-height:21px}
  .features{left:306px;top:85px;width:314px;height:145px;background:var(--coral);padding:14px 14px;list-style:none}
  .features li{color:var(--white);font-weight:700;font-size:17px;line-height:29.5px;white-space:nowrap;display:flex;align-items:center;gap:6px}
  .features svg{flex:none}
  .coupon{left:20px;top:253px;width:598px;height:148px;background:var(--teal);color:var(--white)}
  .coupon-edge{left:4px;top:4px;right:4px;bottom:4px;border:2px dashed rgba(255,255,255,.85)}
  .price{left:14px;top:-14px;font-size:124px;font-weight:600;line-height:1.3;letter-spacing:-2px;white-space:nowrap}
  .price sup{font-size:58px;vertical-align:top;position:relative;top:-4px}
  .offer-title{left:201px;top:16px;font-size:40px;font-weight:500;line-height:1.3;letter-spacing:-.5px;white-space:nowrap}
  .offer-terms{left:201px;top:76px;font-size:21px;line-height:1.2;white-space:nowrap}
</style>
</head>
<body>
<div class="canvas">

  <section class="card card--front">
    <div class="abs band"></div>
    <div class="abs photo photo--family" role="img" aria-label="Photo of a smiling family with their dog"></div>
    <div class="abs photo photo--kitchen" role="img" aria-label="Photo of a bright, clean kitchen"></div>
    <div class="abs hero" role="img" aria-label="Photo of a smiling cleaner in a teal apron holding a mop and bucket, surrounded by soap bubbles"></div>
    <p class="abs text cond kicker">DO YOU REALLY HAVE THE TIME TO TACKLE</p>
    <h1 class="abs text cond headline">HOUSE CHORES?</h1>
    <p class="abs text cond book">BOOK NOW AT <span class="brand">Dustly<small>.COM</small></span></p>
    <p class="abs text url">www.dustly.com/ca39</p>
    <p class="abs text call"><b>or</b> call1-800-8DUSTLY</p>
    <p class="abs text promo">A <sup>$</sup>105 Value! Use Promo Code: CA39</p>
  </section>

  <section class="card card--back">
    <h2 class="abs cond tagline">LET DUSTLY HANDLE IT!</h2>
    <p class="abs logo brand">Dustly<small>.COM</small></p>
    <p class="abs intro">Dustly professionals provide thorough, eco-friendly cleaning services that make your home sparkling clean! Each fully-screened cleaning expert follows a 60-point checklist to ensure spotless results for your home!</p>
    <ul class="abs features">
      <li><svg width="16" height="14" viewBox="0 0 16 14"><path d="M1 8l4 4 10-11" fill="none" stroke="var(--tick)" stroke-width="2.6"/></svg>Eco-Friendly Cleaning Services</li>
      <li><svg width="16" height="14" viewBox="0 0 16 14"><path d="M1 8l4 4 10-11" fill="none" stroke="var(--tick)" stroke-width="2.6"/></svg>Fully-Screened Cleaning Experts</li>
      <li><svg width="16" height="14" viewBox="0 0 16 14"><path d="M1 8l4 4 10-11" fill="none" stroke="var(--tick)" stroke-width="2.6"/></svg>60-point checklist</li>
      <li><svg width="16" height="14" viewBox="0 0 16 14"><path d="M1 8l4 4 10-11" fill="none" stroke="var(--tick)" stroke-width="2.6"/></svg>Easy Online Booking Process</li>
    </ul>
    <div class="abs coupon">
      <div class="abs coupon-edge"></div>
      <p class="abs cond price"><sup>$</sup>39</p>
      <p class="abs cond offer-title">CLEANING FOR 3 HOURS</p>
      <p class="abs offer-terms">Offer good for first time cleaning.<br>Offers expires 11/30/2014</p>
    </div>
  </section>

</div>
</body>
</html>
```